Bref créative
Business card and stationary for Maplecrest Vision Studio Eye Clinic
Maplecrest Vision Studio / (Clear Sight Daily)
Professional
Dr. Marcus Pell, O.D.
Optometric Physician
Bayline Office
2864 Larkwood Ave
Westmarsh, ST. 00417
Emergency:555-014-0487
maplecrestvisionstudiohub@mailbox-demo.net
www.maplecrestvisionstudio-demo.com
Appointment
Date:_______ @ ______ AM / PM
WWW.MAPLECRESTVISIONSTUDIO-DEMO.COM
if unable to keep appointment kindly give 24 hours notice.
I need a business card and brochure made for my office with the new logo.

```html
<!DOCTYPE html>
<html lang="en">
<head>
<meta charset="utf-8">
<title>Maplecrest Vision Studio – Business Card</title>
<link href="https://fonts.googleapis.com/css2?family=Cinzel:wght@600&family=Raleway:wght@400;500;600&display=swap" rel="stylesheet">
<style>
  :root {
    --stage: #e4e5e7;
    --brand-blue: #3b8fc6;
    --brand-navy: #1f4f78;
    --charcoal: #2f3033;
    --ink: #4a4d52;
    --card-white: #fbfbfb;
    --shadow: rgba(0,0,0,0.18);
  }
  * { box-sizing: border-box; margin: 0; padding: 0; }
  html, body { width: 1200px; height: 984px; overflow: hidden; }
  body { background: var(--stage); font-family: "Raleway", sans-serif; position: relative; }

  .card { position: absolute; border-radius: 20px; overflow: hidden; box-shadow: 0 14px 30px var(--shadow); }

  /* Back of card */
  .card-back { left: 330px; top: 56px; width: 640px; height: 366px; background: var(--brand-blue); }
  .card-back .brand-mark { position: absolute; left: 0; right: 0; top: 140px; display: flex; flex-direction: column; align-items: center; gap: 14px; }
  .card-back .brand-dot { width: 34px; height: 34px; border-radius: 50%; background: #fff; }
  .card-back .brand-name { font-family: "Cinzel", serif; font-weight: 600; font-size: 24px; letter-spacing: 3px; color: #fff; }
  .card-back .web-vertical { position: absolute; left: 34px; top: 183px; transform: translate(-50%, -50%) rotate(90deg); white-space: nowrap; font-size: 11px; letter-spacing: 3px; color: #fff; }

  /* Front of card */
  .card-front { left: 220px; top: 478px; width: 760px; height: 440px; background: var(--card-white); }
  .card-front .swoosh { position: absolute; left: 0; top: 0; width: 260px; height: 440px; }
  .front-brand { position: absolute; left: 270px; top: 70px; display: flex; flex-direction: column; align-items: center; width: 340px; }
  .front-brand .brand-head { display: flex; align-items: center; gap: 12px; }
  .front-brand .brand-dot { width: 22px; height: 22px; border-radius: 50%; background: var(--brand-blue); flex: none; }
  .front-brand .brand-name { font-family: "Cinzel", serif; font-weight: 600; font-size: 30px; letter-spacing: 2px; color: var(--brand-navy); text-align: center; line-height: 1.15; }
  .front-brand .tagline { margin-top: 10px; font-size: 17px; color: var(--brand-blue); letter-spacing: 1px; }
  .doctor { position: absolute; left: 250px; top: 250px; }
  .doctor .name { font-size: 15px; font-weight: 600; color: var(--brand-blue); }
  .doctor .title { margin-top: 4px; font-size: 12px; color: var(--ink); letter-spacing: 0.5px; }
  .contacts { position: absolute; left: 430px; top: 290px; list-style: none; display: flex; flex-direction: column; gap: 7px; }
  .contacts li { display: flex; align-items: center; gap: 9px; font-size: 11.5px; color: var(--ink); white-space: nowrap; }
  .contacts .icon { width: 16px; height: 16px; border-radius: 50%; background: var(--brand-blue); display: flex; align-items: center; justify-content: center; flex: none; }
  .contacts .icon svg { width: 9px; height: 9px; fill: #fff; }
</style>
</head>
<body>

<section class="card card-back" aria-label="Business card back">
  <div class="brand-mark">
    <span class="brand-dot"></span>
    <span class="brand-name">MAPLECREST VISION STUDIO</span>
  </div>
  <span class="web-vertical">www.maplecrestvisionstudio-demo.com</span>
</section>

<section class="card card-front" aria-label="Business card front">
  <svg class="swoosh" viewBox="0 0 260 440" aria-hidden="true">
    <path d="M0 0 H215 C115 70 70 230 112 440 H0 Z" fill="var(--brand-blue)"/>
    <path d="M118 120 C92 240 118 350 178 440 H150 C100 360 85 250 118 120 Z" fill="var(--charcoal)"/>
  </svg>

  <div class="front-brand">
    <div class="brand-head">
      <span class="brand-dot"></span>
      <span class="brand-name">MAPLECREST<br>VISION STUDIO</span>
    </div>
    <span class="tagline">Clear Sight Daily</span>
  </div>

  <div class="doctor">
    <p class="name">Dr. Marcus Pell, O.D.</p>
    <p class="title">Optometric Physician</p>
  </div>

  <ul class="contacts">
    <li><span class="icon"><svg viewBox="0 0 10 10"><path d="M5 0a3.5 3.5 0 0 0-3.5 3.5C1.5 6 5 10 5 10s3.5-4 3.5-6.5A3.5 3.5 0 0 0 5 0zm0 5a1.5 1.5 0 1 1 0-3 1.5 1.5 0 0 1 0 3z"/></svg></span>Bayline Office 2864 Larkwood Ave</li>
    <li><span class="icon"><svg viewBox="0 0 10 10"><path d="M5 0a3.5 3.5 0 0 0-3.5 3.5C1.5 6 5 10 5 10s3.5-4 3.5-6.5A3.5 3.5 0 0 0 5 0zm0 5a1.5 1.5 0 1 1 0-3 1.5 1.5 0 0 1 0 3z"/></svg></span>Westmarsh, ST. 00417</li>
    <li><span class="icon"><svg viewBox="0 0 10 10"><path d="M2 0.5l2 2-1 1.2c.6 1.3 1.7 2.4 3 3l1.2-1 2 2L8 9.5C4 9.5 .5 6 .5 2z"/></svg></span>Emergency: 555-014-0487</li>
    <li><span class="icon"><svg viewBox="0 0 10 10"><path d="M0 2h10v6H0z M0 2l5 3.5L10 2" /></svg></span>maplecrestvisionstudiohub@mailbox-demo.net</li>
    <li><span class="icon"><svg viewBox="0 0 10 10"><circle cx="5" cy="5" r="4.5"/></svg></span>www.maplecrestvisionstudio-demo.com</li>
  </ul>
</section>

</body>
</html>
```